quote template for plumbing serivce for homeowners

Design Brief – Plumbing Quotation Document
1. Brand & Style
• Business: Plumbing (Maintenance focus, premium service)
• Positioning: Professional, trustworthy, high-end, compliant, reliable
• Tone: Clean, modern, premium trades, easy to read, confidence-building
• Colours: Use brand colours (or leave placeholders: Primary / Secondary / Accent)
• Fonts:
o Headings: Bold, clean, modern (e.g. Montserrat, Poppins, Inter)
o Body text: Simple and highly readable (e.g. Inter, Lato, Open Sans)
• Layout Feel: Structured, not cluttered, strong hierarchy, visually balanced, logical flow
• Imagery: Minimal – allow subtle plumbing or technical icons, but do not overpower text
2. Document Requirements
✅ Must Include:
Cover Page
• Logo
• Business name
• Tagline (if applicable)
• Document title: Quotation / Proposal
• Client name, site address, quote number, date
• Business contact details (phone, email, website, licence number optional)
• Optional photo banner or design strip (clean and minimal)
Section 1 – Introduction
• Short professional message thanking them, setting expectations
• Optional small “Our promise” or “What to expect” note
Section 2 – Price Options
• Must support unlimited quote sections / options (Option 1, Option 2, Option 3 etc.)
• Each option should include:
o Detailed description
o Price
o Optional tick/check icons to highlight benefits
• Layout must allow adding or removing options easily without breaking format
• Pricing to be emphasised but not overpower the description
Section 3 – Total Investment
• Clearly display:
o Subtotal
o GST
o Total
• Include optional line for:
o Deposit (if applicable)
o Payment terms (optional)
• Should stand out using contrast box or section highlight
Section 4 – Why Choose Us
Include space or icons for key trust points. Must allow content similar to:
• Licensed & insured plumbing professionals
• Lifetime labour warranty on workmanship
• Premium materials and compliant installations
• Transparent pricing, no hidden surprises
• On-time, tidy, and customer-focused
• Australian Standards compliant (AS/NZS 3500)
• Local, trusted, reviewed business
Designer to create layout that supports 5–8 trust points using icons or bold highlights.
Section 5 – Terms & Conditions
Must allow a text area for:
• Quote validity
• What is/what isn’t included
• Warranty notes
• Site access requirements
• Variations clause
• Payment terms
Section 6 – Acceptance
Needs to include:
• Signature line
• Print name
• Date
• Option to tick selected option if multiple options provided
• “Approval to proceed” section
Optional Page Elements
(Include if space allows)
• Certifications or licence numbers
• Quorvix review rating or testimonial section
• Before/after photo box (if relevant)
• QR code linking to website or booking page
• Small footer with company details on each page
3. Functional Requirements
• Must be:
o Easy to edit (headings, prices, options, text blocks)
o Expandable (sections must duplicate without breaking layout)
o Saveable as PDF
o Professional when printed
o Visually aligned to premium home & commercial clients
• Page numbering required (Page 1 of X)
• Consistent header or footer with business name/logo
4. Deliverables Needed
Designer to supply:
1. Master editable template (Canva, Word, or InDesign INDD)
2. PDF export version
3. Style guide (fonts, sizes, colours)
4. Instructions for duplicating option sections easily
5. Design Inspiration Keywords
• Premium trade proposal
• Clean modern layout
• Structured price options
• Trust-building visuals
• Technical but customer-friendly
• Compliant and confident
home owners
plumbing

```html
<!DOCTYPE html>
<html lang="en">
<head>
<meta charset="utf-8">
<title>Kestrel Plumbing – Quotation Template</title>
<link href="https://fonts.googleapis.com/css2?family=Poppins:wght@400;500;600;700;800&display=swap" rel="stylesheet">
<style>
:root{
  --backdrop:#c9cacc;
  --paper:#ffffff;
  --cyan:#2bb8e3;
  --blue:#0b6bd9;
  --navy:#0a4fa8;
  --yellow:#f5bd3b;
  --ink:#2b2b2b;
  --muted:#6b6f75;
  --rule:#e6e8eb;
  --panel:#eeeff1;
}
*{margin:0;padding:0;box-sizing:border-box}
html,body{width:1200px;height:617px;overflow:hidden;background:var(--backdrop);font-family:'Poppins',sans-serif;color:var(--ink)}
.canvas{position:relative;width:1200px;height:617px}
.page{position:absolute;background:var(--paper);overflow:hidden;box-shadow:0 1px 4px rgba(0,0,0,.18)}
.abs{position:absolute}
.heading{position:absolute;left:14px;color:var(--cyan);font-weight:600;font-size:7px}
.body{font-size:3px;line-height:4.4px;color:var(--muted)}
.white{color:#fff}
/* footer */
.footer{position:absolute;left:14px;right:14px;height:6px;display:flex;align-items:center;gap:3px}
.footer .mark{font-size:4px;font-weight:700;color:var(--cyan);letter-spacing:.1px}
.footer .url{background:var(--yellow);border-radius:3px;font-size:2.2px;padding:.6px 3px;color:var(--ink)}
.footer .line{flex:1;height:.4px;background:var(--cyan);opacity:.6}
.footer .num{font-size:2.6px;color:var(--ink)}
.footer.on-cyan .mark{color:#fff}
.footer.on-cyan .line{background:#fff}
.footer.on-cyan .num{color:#fff}
/* cover */
.brand{position:absolute;left:0;right:0;top:14px;text-align:center;color:var(--cyan);font-weight:800;line-height:1}
.brand .big{font-size:25px;letter-spacing:1px}
.brand .small{font-size:8.5px;letter-spacing:1.6px;margin-top:2px}
.biz-name{position:absolute;left:28px;top:64px;font-size:19.5px;font-weight:800;color:var(--cyan);letter-spacing:.2px}
.tagline{position:absolute;left:28px;top:88px;width:153px;height:6px;background:var(--yellow);color:#fff;font-size:3.4px;letter-spacing:3px;text-align:center;line-height:6px}
.meta{position:absolute;font-size:4px;font-weight:600;color:var(--ink)}
.meta span{font-weight:400}
.contact{position:absolute;font-size:3.6px;font-weight:600;color:#fff;display:flex;align-items:center;gap:2px}
.contact i{display:inline-block;width:4px;height:4px;border-radius:50%;background:var(--yellow)}
/* photos */
.photo{position:absolute}
/* price rows */
.opt{position:absolute;left:14px;width:179px;height:30px;background:var(--panel)}
.opt .label{position:absolute;left:0;top:0;width:36px;height:30px;padding:3px 3px;color:#fff}
.opt .label b{display:block;font-size:5px;font-weight:600}
.opt .label p{font-size:2.3px;line-height:3.2px;margin-top:3px}
.opt .label::after{content:"";position:absolute;right:-3px;top:12px;border-left:3px solid var(--c);border-top:3px solid transparent;border-bottom:3px solid transparent}
.opt .items{position:absolute;top:5px;display:flex;flex-direction:column;gap:5.2px}
.opt .items div{font-size:2.2px;color:var(--muted);display:flex;gap:1.5px;align-items:center;border-bottom:.3px solid #d6d8db;width:50px;padding-bottom:.6px}
.opt .items div::before{content:"";width:2px;height:2px;border-radius:50%;border:.3px solid var(--cyan)}
.opt .price{position:absolute;right:0;top:0;width:22px;height:30px;background:var(--cyan);color:#fff;font-size:5px;font-weight:600;display:flex;align-items:center;justify-content:center}
/* investment */
.table-head{position:absolute;left:14px;width:180px;top:33px;height:8.5px;background:var(--blue);border-radius:1.5px;color:#fff;font-size:3.6px;display:flex;align-items:center}
.table-row{position:absolute;left:14px;width:180px;height:9px;border:.4px solid var(--rule);border-radius:1.5px}
.label-sm{position:absolute;font-size:3.6px;color:var(--ink)}
.label-bold{position:absolute;font-size:4px;font-weight:600;color:var(--ink)}
.total-box{position:absolute;left:139px;top:162px;width:55px;height:8px;background:var(--blue);color:#fff;font-size:3.6px;line-height:8px;padding-left:6px}
/* why choose */
.trust-bar{position:absolute;left:0;top:32px;width:26px;height:210px;background:var(--blue)}
.trust{position:absolute;left:20px;width:176px;height:14px}
.trust .tab{position:absolute;left:0;top:3px;width:14px;height:8px;background:#e2e3e5}
.trust .strip{position:absolute;left:31px;top:2px;right:0;height:10px;background:var(--panel);font-size:3.4px;line-height:10px;padding-left:6px}
.trust .icon{position:absolute;left:12px;top:-3px;width:20px;height:20px;border-radius:50%;background:var(--yellow);border:1.2px solid #fff;box-shadow:0 0 0 .5px #e0a829}
.trust .icon svg{position:absolute;left:5px;top:5px;width:8px;height:8px}
/* terms */
.sub{position:absolute;left:14px;font-size:4.6px;font-weight:600;color:var(--blue)}
.sub-rule{position:absolute;left:14px;width:175px;height:.4px;background:var(--cyan)}
.mini{position:absolute;left:14px;font-size:3.3px;color:var(--cyan);font-weight:500}
.txt{position:absolute;left:14px;width:178px}
/* acceptance */
.check{position:absolute;left:14px;font-size:3.4px;color:var(--muted);display:flex;align-items:center;gap:2.5px}
.check i{width:2.8px;height:2.8px;border:.35px solid #9aa0a6;display:inline-block}
/* testimonials */
.quote-card{position:absolute;left:14px;width:183px;height:36px;background:var(--blue);border-radius:2px}
.quote-card p{position:absolute;left:8px;right:20px;top:19px;font-size:3.2px;line-height:4.6px;color:#fff}
.avatar{position:absolute;left:91px;width:28px;height:28px;margin-left:-14px;border-radius:50%;border:1.2px solid #fff;background:linear-gradient(160deg,#7b6858,#3f3a38)}
.qmark{position:absolute;width:12px;height:12px;border-radius:50%;background:var(--cyan);border:1px solid #fff;color:#fff;font-size:7px;font-weight:700;font-style:italic;text-align:center;line-height:12px}
.ba-label{position:absolute;top:33px;font-size:7px;font-weight:600;color:var(--ink);width:88px;text-align:center}
</style>
</head>
<body>
<div class="canvas">

<!-- ============ Cover ============ -->
<section class="page cover" style="left:28px;top:23px;width:210px;height:272px">
  <div class="brand"><div class="big">KESTREL</div><div class="small">PLUMBING</div></div>
  <div class="biz-name">BUSINESS NAME</div>
  <div class="tagline">TAGLINE HERE</div>
  <div class="meta" style="left:28px;top:102px">Document title: <span>Quotation / Proposal</span></div>
  <div class="meta" style="left:28px;top:114px">Client Name:</div>
  <div class="meta" style="left:110px;top:114px">Site Address:</div>
  <div class="meta" style="left:28px;top:124px">Quote Number:</div>
  <div class="meta" style="left:110px;top:124px">Date:</div>
  <svg class="abs" style="left:0;top:0" width="210" height="272" viewBox="0 0 210 272" aria-hidden="true">
    <defs>
      <linearGradient id="coverPhoto" x1="0" y1="0" x2="1" y2="1">
        <stop offset="0" stop-color="#d9d6d2"/><stop offset=".55" stop-color="#8a7d70"/><stop offset="1" stop-color="#3b3633"/>
      </linearGradient>
    </defs>
    <path d="M0,272 L0,212 C40,170 110,150 165,158 C190,162 204,172 210,186 L210,272 Z" fill="#2bb8e3"/>
    <path d="M0,272 C20,222 70,186 140,178 C110,196 82,228 70,272 Z" fill="#f5bd3b"/>
    <path d="M196,210 C190,230 178,250 160,272 L210,272 L210,200 Z" fill="#f5bd3b"/>
    <path d="M128,200 L196,128" stroke="#2bb8e3" stroke-width="6" stroke-linecap="round"/>
    <path d="M184,126 L204,116 L198,137 Z" fill="#2bb8e3"/>
  </svg>
  <div class="photo" role="img" aria-label="Plumber kneeling beside a tool bag in a modern kitchen" style="left:65px;top:168px;width:170px;height:170px;border-radius:50%;background:linear-gradient(145deg,#e2dfdb,#9c8f82 55%,#3f3935)"></div>
  <div class="contact" style="left:75px;top:244px"><i></i>0123-456-789</div>
  <div class="contact" style="left:138px;top:244px"><i></i>www.dummywebsite.com</div>
  <div class="contact" style="left:75px;top:253px"><i></i>dummy mail@here.com</div>
  <div class="contact" style="left:138px;top:253px"><i></i>licence Number</div>
</section>

<!-- ============ Introduction ============ -->
<section class="page intro" style="left:260px;top:25px;width:209px;height:270px">
  <div class="abs" style="left:0;top:138px;width:209px;height:132px;background:var(--cyan)"></div>
  <div class="photo" role="img" aria-label="Plumber installing a fixture in a bathroom" style="left:0;top:14px;width:66px;height:171px;border-radius:0 3px 3px 0;background:linear-gradient(170deg,#cfd0d2,#7d7771 55%,#3a3634)"></div>
  <div class="heading" style="left:75px;top:13px">Introduction</div>
  <div class="abs body" style="left:75px;top:31px;width:122px">Lorem Ipsum is simply dummy text of the printing and typesetting industry. Lorem Ipsum has been the industry's standard dummy text ever since the 1500s, when an unknown printer took a galley of type and scrambled it to make a type specimen book.<br><br>There are many variations of passages of Lorem Ipsum available, but the majority have suffered alteration in some form, by injected humour, or randomised words which don't look even slightly believable. If you are going to use a passage of Lorem Ipsum, you need to be sure there isn't anything embarrassing hidden in the middle of text.<br><br>All the Lorem Ipsum generators on the Internet tend to repeat predefined chunks as necessary, making this the first true generator on the Internet. It uses a dictionary of over 200 Latin words, combined with a handful of model sentence structures, to generate Lorem Ipsum which looks reasonable.</div>
  <div class="heading white" style="left:75px;top:145px">Our Promise</div>
  <div class="abs white" style="left:75px;top:160px;width:122px;font-size:3.3px;line-height:4.7px;font-weight:600">Lorem Ipsum is simply dummy text of the printing and typesetting industry. Lorem Ipsum has been the industry's standard dummy text ever since the 1500s, when an unknown printer took a galley of type and scrambled it to make a type specimen book.</div>
  <div class="abs body white" style="left:14px;top:204px;width:182px">All the Lorem Ipsum generators on the Internet tend to repeat predefined chunks as necessary, making this the first true generator on the Internet. It uses a dictionary of over 200 Latin words, combined with a handful of model sentence structures, to generate Lorem Ipsum which looks reasonable. The generated Lorem Ipsum is therefore always free from repetition, injected humour, or non-characteristic words etc.</div>
  <div class="footer on-cyan" style="top:252px"><span class="mark">KESTREL</span><span class="url">www.kestrelplumbing.com.au</span><span class="line"></span><span class="num">02</span></div>
</section>

<!-- ============ Price Options ============ -->
<section class="page prices" style="left:492px;top:25px;width:208px;height:270px">
  <div class="heading" style="top:13px">Price Options</div>

  <div class="opt" style="top:29px;--c:#0a4fa8"><div class="label" style="background:#0a4fa8"><b>Option 1</b><p>Lorem ipsum is simply dummy text of the printing.</p></div>
    <div class="items" style="left:46px"><div>Lorem ipsum is dummy text.</div><div>Lorem ipsum is dummy text.</div><div>Lorem ipsum is dummy text.</div></div>
    <div class="items" style="left:105px"><div>Lorem ipsum is dummy text.</div><div>Lorem ipsum is dummy text.</div><div>Lorem ipsum is dummy text.</div></div>
    <div class="price">$XXX</div></div>

  <div class="opt" style="top:65px;--c:#0b6bd9"><div class="label" style="background:#0b6bd9"><b>Option 1</b><p>Lorem ipsum is simply dummy text of the printing.</p></div>
    <div class="items" style="left:46px"><div>Lorem ipsum is dummy text.</div><div>Lorem ipsum is dummy text.</div><div>Lorem ipsum is dummy text.</div></div>
    <div class="items" style="left:105px"><div>Lorem ipsum is dummy text.</div><div>Lorem ipsum is dummy text.</div><div>Lorem ipsum is dummy text.</div></div>
    <div class="price">$XXX</div></div>

  <div class="opt" style="top:101px;--c:#2a7fe0"><div class="label" style="background:#2a7fe0"><b>Option 1</b><p>Lorem ipsum is simply dummy text of the printing.</p></div>
    <div class="items" style="left:46px"><div>Lorem ipsum is dummy text.</div><div>Lorem ipsum is dummy text.</div><div>Lorem ipsum is dummy text.</div></div>
    <div class="items" style="left:105px"><div>Lorem ipsum is dummy text.</div><div>Lorem ipsum is dummy text.</div><div>Lorem ipsum is dummy text.</div></div>
    <div class="price">$XXX</div></div>

  <div class="opt" style="top:137px;--c:#4f98e8"><div class="label" style="background:#4f98e8"><b>Option 1</b><p>Lorem ipsum is simply dummy text of the printing.</p></div>
    <div class="items" style="left:46px"><div>Lorem ipsum is dummy text.</div><div>Lorem ipsum is dummy text.</div><div>Lorem ipsum is dummy text.</div></div>
    <div class="items" style="left:105px"><div>Lorem ipsum is dummy text.</div><div>Lorem ipsum is dummy text.</div><div>Lorem ipsum is dummy text.</div></div>
    <div class="price">$XXX</div></div>

  <div class="opt" style="top:173px;--c:#78b2ef"><div class="label" style="background:#78b2ef"><b>Option 1</b><p>Lorem ipsum is simply dummy text of the printing.</p></div>
    <div class="items" style="left:46px"><div>Lorem ipsum is dummy text.</div><div>Lorem ipsum is dummy text.</div><div>Lorem ipsum is dummy text.</div></div>
    <div class="items" style="left:105px"><div>Lorem ipsum is dummy text.</div><div>Lorem ipsum is dummy text.</div><div>Lorem ipsum is dummy text.</div></div>
    <div class="price">$XXX</div></div>

  <div class="opt" style="top:209px;--c:#a3cbf4"><div class="label" style="background:#a3cbf4"><b>Option 1</b><p>Lorem ipsum is simply dummy text of the printing.</p></div>
    <div class="items" style="left:46px"><div>Lorem ipsum is dummy text.</div><div>Lorem ipsum is dummy text.</div><div>Lorem ipsum is dummy text.</div></div>
    <div class="items" style="left:105px"><div>Lorem ipsum is dummy text.</div><div>Lorem ipsum is dummy text.</div><div>Lorem ipsum is dummy text.</div></div>
    <div class="price">$XXX</div></div>

  <div class="footer" style="top:251px"><span class="mark">KESTREL</span><span class="url">www.kestrelplumbing.com.au</span><span class="line"></span><span class="num">03</span></div>
</section>

<!-- ============ Total Investment ============ -->
<section class="page investment" style="left:722px;top:25px;width:208px;height:270px">
  <div class="heading" style="top:13px">Total Investment</div>
  <div class="table-head"><span style="width:10%;padding-left:5px">SL</span><span style="width:42%">Item Description</span><span style="width:18%">Price</span><span style="width:17%">Qty.</span><span>Total</span></div>
  <div class="table-row" style="top:45px"></div>
  <div class="table-row" style="top:58px"></div>
  <div class="table-row" style="top:72px"></div>
  <div class="table-row" style="top:85px"></div>
  <div class="table-row" style="top:99px"></div>
  <div class="table-row" style="top:112px"></div>
  <div class="label-bold" style="left:14px;top:131px">Payment Info:</div>
  <div class="label-sm" style="left:14px;top:142px">Account No&nbsp;&nbsp;&nbsp;:</div>
  <div class="label-sm" style="left:14px;top:149px">A/C Name&nbsp;&nbsp;&nbsp;&nbsp;&nbsp;&nbsp;:</div>
  <div class="label-sm" style="left:14px;top:156px">Branch Name&nbsp;:</div>
  <div class="label-sm" style="left:145px;top:142px">Sub Total :</div>
  <div class="label-sm" style="left:145px;top:149px">Discount&nbsp;&nbsp;:</div>
  <div class="label-sm" style="left:145px;top:156px">GST&nbsp;&nbsp;&nbsp;&nbsp;&nbsp;&nbsp;&nbsp;&nbsp;&nbsp;:</div>
  <div class="total-box">Total&nbsp;&nbsp;&nbsp;&nbsp;&nbsp;:</div>
  <div class="label-bold" style="left:14px;top:169px">Terms &amp; Conditions:</div>
  <div class="abs body" style="left:14px;top:178px;width:62px">Lorem Ipsum is simply dummy text of the printing and typesetting industry.</div>
  <div class="footer" style="top:251px"><span class="mark">KESTREL</span><span class="url">www.kestrelplumbing.com.au</span><span class="line"></span><span class="num">04</span></div>
</section>

<!-- ============ Why Choose Us ============ -->
<section class="page why" style="left:958px;top:23px;width:211px;height:273px">
  <div class="heading" style="top:13px">Why Choose Us</div>
  <div class="trust-bar"></div>
  <div class="trust" style="top:37px"><span class="tab"></span><span class="strip">Licensed &amp; insured plumbing professionals.</span><span class="icon"><svg viewBox="0 0 8 8" fill="none" stroke="#2b2b2b" stroke-width=".6"><rect x="1" y=".8" width="5" height="6.4"/><path d="M2 2.5h3M2 4h3M2 5.5h1.5"/></svg></span></div>
  <div class="trust" style="top:67px"><span class="tab"></span><span class="strip">Lifetime labour warranty on workmanship.</span><span class="icon"><svg viewBox="0 0 8 8" fill="none" stroke="#2b2b2b" stroke-width=".6"><circle cx="4" cy="3.6" r="2.6"/><path d="M2.8 3.6l.9.9 1.6-1.7"/></svg></span></div>
  <div class="trust" style="top:97px"><span class="tab"></span><span class="strip">Premium materials and compliant installations.</span><span class="icon"><svg viewBox="0 0 8 8" fill="none" stroke="#2b2b2b" stroke-width=".6"><path d="M1 6.5h3V4h2.5V1.5"/><path d="M5.5 1.5h2"/></svg></span></div>
  <div class="trust" style="top:127px"><span class="tab"></span><span class="strip">Transparent pricing, no hidden surprises.</span><span class="icon"><svg viewBox="0 0 8 8" fill="none" stroke="#2b2b2b" stroke-width=".6"><ellipse cx="4" cy="2.5" rx="3" ry="1.1"/><path d="M1 2.5v3c0 .6 1.3 1.1 3 1.1s3-.5 3-1.1v-3M1 4c0 .6 1.3 1.1 3 1.1S7 4.6 7 4"/></svg></span></div>
  <div class="trust" style="top:157px"><span class="tab"></span><span class="strip">On-time, tidy, and customer-focused.</span><span class="icon"><svg viewBox="0 0 8 8" fill="none" stroke="#2b2b2b" stroke-width=".6"><circle cx="2.3" cy="3" r="1"/><circle cx="5.7" cy="3" r="1"/><path d="M.6 6.5c.3-1.2 3.1-1.2 3.4 0M4 6.5c.3-1.2 3.1-1.2 3.4 0"/></svg></span></div>
  <div class="trust" style="top:187px"><span class="tab"></span><span class="strip">Australian Standards compliant (AS/NZS 3500).</span><span class="icon"><svg viewBox="0 0 8 8" fill="none" stroke="#2b2b2b" stroke-width=".6"><rect x="1" y=".8" width="5" height="6.4"/><path d="M2.2 4l1 1 1.8-2"/></svg></span></div>
  <div class="trust" style="top:217px"><span class="tab"></span><span class="strip">Local, trusted, reviewed business.</span><span class="icon"><svg viewBox="0 0 8 8" fill="none" stroke="#2b2b2b" stroke-width=".6"><path d="M4 7.2S1.4 4.6 1.4 3a2.6 2.6 0 015.2 0c0 1.6-2.6 4.2-2.6 4.2z"/><circle cx="4" cy="3" r=".9"/></svg></span></div>
  <div class="footer" style="top:253px"><span class="mark">KESTREL</span><span class="url">www.kestrelplumbing.com.au</span><span class="line"></span><span class="num">05</span></div>
</section>

<!-- ============ Terms & Conditions ============ -->
<section class="page terms" style="left:32px;top:314px;width:203px;height:262px">
  <div class="heading" style="top:13px">Terms &amp; Conditions</div>
  <div class="txt" style="top:31px;font-size:3.3px;line-height:4.5px;font-weight:600;color:var(--ink)">Lorem Ipsum is simply dummy text of the printing and typesetting industry. Lorem Ipsum has been the industry's standard dummy text.</div>
  <div class="sub" style="top:46px">Exclusions</div><div class="sub-rule" style="top:54px"></div>
  <div class="mini" style="top:60px">What's Included:</div>
  <div class="txt body" style="top:67px">There are many variations of passages of Lorem Ipsum available, but the majority have suffered alteration in some form, by injected humour, or randomised words which don't look even slightly believable.</div>
  <div class="mini" style="top:82px">What's Not Included:</div>
  <div class="txt body" style="top:89px">There are many variations of passages of Lorem Ipsum available, but the majority have suffered alteration in some form, by injected humour, or randomised words which don't look even slightly believable.</div>
  <div class="sub" style="top:107px">Warranty Notes</div><div class="sub-rule" style="top:115px"></div>
  <div class="txt body" style="top:121px">There are many variations of passages of Lorem Ipsum available, but the majority have suffered alteration in some form, by injected humour, or randomised words which don't look even slightly believable.</div>
  <div class="sub" style="top:139px">Site Access Requirements</div><div class="sub-rule" style="top:147px"></div>
  <div class="txt body" style="top:153px">There are many variations of passages of Lorem Ipsum available, but the majority have suffered alteration in some form, by injected humour, or randomised words which don't look even slightly believable.</div>
  <div class="sub" style="top:171px">Variations Clause</div><div class="sub-rule" style="top:179px"></div>
  <div class="txt body" style="top:185px">There are many variations of passages of Lorem Ipsum available, but the majority have suffered alteration in some form, by injected humour, or randomised words which don't look even slightly believable.</div>
  <div class="sub" style="top:203px">Payment Terms</div><div class="sub-rule" style="top:211px"></div>
  <div class="txt body" style="top:217px">There are many variations of passages of Lorem Ipsum available, but the majority have suffered alteration in some form, by injected humour, or randomised words which don't look even slightly believable.</div>
  <div class="footer" style="top:245px"><span class="mark">KESTREL</span><span class="url">www.kestrelplumbing.com.au</span><span class="line"></span><span class="num">06</span></div>
</section>

<!-- ============ Acceptance ============ -->
<section class="page acceptance" style="left:259px;top:314px;width:208px;height:269px">
  <div class="heading" style="top:13px">Acceptance</div>
  <div class="label-bold" style="left:14px;top:32px;font-size:3.6px">Date:</div>
  <div class="label-bold" style="left:14px;top:43px;font-size:3.6px">Name Here</div>
  <div class="abs body" style="left:14px;top:49px">imply dummy text 2A,<br>Lorem Ipsum- 000213</div>
  <div class="abs body" style="left:14px;top:66px">Dear Mr/Mrs. ..................</div>
  <div class="abs body" style="left:14px;top:80px;width:180px;font-size:3.3px;line-height:5.2px">Lorem Ipsum is simply dummy text of the printing and typesetting industry. Lorem Ipsum has been the industry's standard dummy text ever since the 1500s, when an unknown printer took a galley of type and scrambled it to make a type specimen book. It has survived not only five centuries, but also the leap into electronic typesetting, remaining essentially unchanged. It was popularised in the 1960s with the release of Letraset sheets containing Lorem Ipsum passages, and more recently with desktop publishing software like Aldus PageMaker including versions of Lorem Ipsum.</div>
  <div class="abs body" style="left:14px;top:118px;width:180px;font-size:3.3px;line-height:5.2px">Lorem Ipsum is simply dummy text of the printing and typesetting industry. Lorem Ipsum has been the industry's standard dummy text ever since the 1500s, when an unknown printer took a galley of type and scrambled it to make a type specimen book.</div>
  <div class="check" style="top:140px"><i></i>Lorem Ipsum is simply dummy text of the printing and typesetting industry.</div>
  <div class="check" style="top:149px"><i></i>Lorem Ipsum is simply dummy text of the printing and typesetting industry.</div>
  <div class="check" style="top:158px"><i></i>Lorem Ipsum is simply dummy text of the printing and typesetting industry.</div>
  <div class="check" style="top:166px"><i></i>Lorem Ipsum is simply dummy text of the printing and typesetting industry.</div>
  <div class="check" style="top:175px"><i></i>Lorem Ipsum is simply dummy text of the printing and typesetting industry.</div>
  <div class="abs" style="left:14px;top:188px;width:180px;font-size:3.4px;line-height:5.2px;font-weight:600;color:var(--ink)">Lorem Ipsum is simply dummy text of the printing and typesetting industry. Lorem Ipsum has been the industry's standard dummy text ever since the 1500s, when an unknown printer took a galley of type and scrambled it to make a type specimen book.</div>
  <div class="label-bold" style="left:14px;top:223px;font-size:3.6px">Signature</div>
  <div class="footer" style="top:252px"><span class="mark">KESTREL</span><span class="url">www.kestrelplumbing.com.au</span><span class="line"></span><span class="num">06</span></div>
</section>

<!-- ============ Testimonials ============ -->
<section class="page testimonials" style="left:489px;top:311px;width:212px;height:274px">
  <div class="heading" style="top:13px">Testimonials</div>
  <div class="quote-card" style="top:48px"><p>Lorem ipsum dolor sit amet, consectetur adipiscing eLorem Ipsum is simply dummy text of the printing and typesetting industry.</p></div>
  <div class="avatar" role="img" aria-label="Customer portrait" style="top:34px;left:105px"></div>
  <div class="qmark" style="left:23px;top:42px">“</div><div class="qmark" style="left:173px;top:78px">”</div>

  <div class="quote-card" style="top:120px"><p>Lorem ipsum dolor sit amet, consectetur adipiscing eLorem Ipsum is simply dummy text of the printing and typesetting industry.</p></div>
  <div class="avatar" role="img" aria-label="Customer portrait" style="top:106px;left:105px"></div>
  <div class="qmark" style="left:23px;top:114px">“</div><div class="qmark" style="left:173px;top:150px">”</div>

  <div class="quote-card" style="top:191px"><p>Lorem ipsum dolor sit amet, consectetur adipiscing eLorem Ipsum is simply dummy text of the printing and typesetting industry.</p></div>
  <div class="avatar" role="img" aria-label="Customer portrait" style="top:177px;left:105px"></div>
  <div class="qmark" style="left:23px;top:185px">“</div><div class="qmark" style="left:173px;top:221px">”</div>
  <div class="footer" style="top:257px"><span class="mark">KESTREL</span><span class="url">www.kestrelplumbing.com.au</span><span class="line"></span><span class="num">07</span></div>
</section>

<!-- ============ Before / After ============ -->
<section class="page before-after" style="left:719px;top:314px;width:215px;height:278px">
  <div class="heading" style="top:13px">Testimonials</div>
  <div class="ba-label" style="left:15px">Before</div>
  <div class="ba-label" style="left:112px">After</div>
  <div class="photo" role="img" aria-label="Before: exposed wall cavity with old drain pipe" style="left:15px;top:54px;width:88px;height:80px;background:linear-gradient(135deg,#c9a589,#7a5438 55%,#3d2a20)"></div>
  <div class="photo" role="img" aria-label="After: new black drain pipe fitted in the wall cavity" style="left:112px;top:54px;width:88px;height:80px;background:linear-gradient(135deg,#c9a589,#6f4c34 50%,#1f1f22)"></div>
  <div class="photo" role="img" aria-label="Before: stripped bathroom with underfloor pipework" style="left:15px;top:155px;width:88px;height:80px;background:linear-gradient(160deg,#e8e4e0,#a89d93 55%,#6d6159)"></div>
  <div class="photo" role="img" aria-label="After: finished bathroom with tiled floor, corner bath and towel rail" style="left:112px;top:155px;width:88px;height:80px;background:linear-gradient(160deg,#ececeb,#c9c8c6 55%,#9d9c9a)"></div>
  <div class="footer" style="top:259px"><span class="mark">KESTREL</span><span class="url">www.kestrelplumbing.com.au</span><span class="line"></span><span class="num">08</span></div>
</section>

</div>
</body>
</html>
```